Nimbrel Computer Solutions
Business Technology Consulting
Professional
Gerald Pinto
1837 NE 41st Court
Lakeport, FL 33971
gerald@nimbrelcs.com
www.nimbrelcs.com
My company file logo. Please contact me if another format is needed.

```html
<!DOCTYPE html>
<html lang="en">
<head>
<meta charset="utf-8">
<title>Nimbrel Computer Solutions – Business Cards</title>
<link rel="stylesheet" href="https://fonts.googleapis.com/css2?family=Arimo:wght@400;700&display=swap">
<style>
  :root {
    --backdrop: #e4e2de;
    --card: #ffffff;
    --card-shade: #e9eaec;
    --band-dark: #0a4f94;
    --band-mid: #1673c4;
    --band-light: #5cb2ea;
    --gold: #d7a928;
    --brand-blue: #1b5ea6;
    --ink: #333a40;
    --faint: rgba(27, 94, 166, 0.07);
  }
  * { margin: 0; padding: 0; box-sizing: border-box; }
  html, body { width: 1200px; height: 902px; overflow: hidden; }
  body {
    background: var(--backdrop);
    font-family: "Arimo", Arial, sans-serif;
    position: relative;
  }
  .card {
    position: absolute;
    width: 556px;
    height: 317px;
    border-radius: 16px;
    background: linear-gradient(180deg, var(--card) 55%, var(--card-shade) 100%);
    box-shadow: 0 6px 18px rgba(0, 0, 0, 0.25);
    overflow: hidden;
  }
  .card-back { left: 447px; top: 442px; }
  .card-front { left: 159px; top: 154px; z-index: 2; }

  .name-band {
    position: absolute;
    left: 0; top: 37px;
    width: 100%; height: 53px;
    background: linear-gradient(90deg, var(--band-dark) 0%, var(--band-mid) 55%, var(--band-light) 100%);
    border-bottom: 5px solid var(--gold);
  }
  .holder-name {
    position: absolute;
    left: 66px; top: 50%;
    transform: translateY(-50%);
    color: #fff;
    font-weight: 700;
    font-size: 25px;
  }
  .brand {
    position: absolute;
    left: 40px; top: 140px;
    width: 230px;
    text-align: center;
  }
  .brand-dot {
    display: block;
    width: 70px; height: 70px;
    margin: 0 auto 8px;
    border-radius: 50%;
    background: var(--brand-blue);
  }
  .brand-name {
    color: var(--brand-blue);
    font-weight: 700;
    font-size: 22px;
    line-height: 1.15;
  }
  .contact {
    position: absolute;
    left: 305px; top: 162px;
    color: var(--ink);
    font-size: 15px;
    line-height: 17px;
  }
  .contact p { white-space: nowrap; }
  .contact .gap { margin-top: 17px; }

  .back-mark {
    position: absolute;
    left: 20px; top: -5px;
    width: 280px; height: 280px;
    border-radius: 50%;
    background: var(--faint);
  }
  .back-brand {
    position: absolute;
    right: 24px; bottom: 36px;
    text-align: center;
  }
  .back-dot {
    display: block;
    width: 72px; height: 72px;
    margin: 0 auto 6px;
    border-radius: 50%;
    background: var(--brand-blue);
  }
  .back-name {
    color: var(--brand-blue);
    font-weight: 700;
    font-size: 14px;
  }
  .back-url {
    position: absolute;
    right: 24px; bottom: 16px;
    color: var(--ink);
    font-size: 13px;
    letter-spacing: 0.5px;
  }
</style>
</head>
<body>
  <section class="card card-back" aria-label="Card back">
    <div class="back-mark"></div>
    <div class="back-brand">
      <span class="back-dot"></span>
      <span class="back-name">Nimbrel</span>
    </div>
    <p class="back-url">www.nimbrelcs.com</p>
  </section>

  <section class="card card-front" aria-label="Card front">
    <div class="name-band">
      <h1 class="holder-name">Gerald Pinto</h1>
    </div>
    <div class="brand">
      <span class="brand-dot"></span>
      <p class="brand-name">Nimbrel<br>Computer Solutions</p>
    </div>
    <div class="contact">
      <p>1837 NE 41st Court</p>
      <p>Lakeport, FL 33971</p>
      <p class="gap">Phone: 239-555-0147</p>
      <p>Email: gerald@nimbrelcs.com</p>
      <p class="gap">www.nimbrelcs.com</p>
    </div>
  </section>
</body>
</html>
```